依頼詳細
ダイナミックなチラシとポスターをお願いします。
見ただけで「すごい!講演に行ってみたい!!」と思えるような。
記載項目
添付資料のとおり
サイズ
A2ポスターとA4チラシ
ページ数
片面
希望イメージ
シンプル 複雑
単色 カラフル
暗い 明るい
日常 高級
遊び心 厳粛
未来的 伝統的
女性的 男性的
納品ファイル
• 高解像度JPG (.jpg)
• イラストレーター形式 (.ai)
補足説明
開催内容の資料を送ります。
また、講師のプロフィールを送ります。

クレジットは、写真提供:森川拓事務所もしくは(c)Taku Morikawa Office等とご表記ください。
皆様お世話になっております。

ポスターの写真は、スポンサーの関係で前回添付した画像以外は基本的には、使用ができませんのでご了承ください。
そのほかの写真を使いたい場合は、一度こちらに確認いただきます様よろしくお願いします。
皆様いつもお世話になっております。
画像が添付されておりませんでした。大変失礼しました。

ご対応どうぞよろしくお願いします。
左上にPRVマークをつけていただきます様よろしくお願いします。
なお、空白とマークの位置はデータのバランスを維持していただきます様お願いします。
■ 選んだ理由

全体の色合いも非常によかったです。ダイナミックな雰囲気と仲間の絆のイメージをうまく表現していただけたと思います。

■ 提案者全員のお礼・コメント

皆様、たくさんのご応募ありがとうございました。こちらのイメージをうまく呼んでいただいたかと思います。
次回もどうぞよろしくお願いします。

```html
<!DOCTYPE html>
<html lang="ja">
<head>
<meta charset="utf-8">
<title>森川拓 講演会</title>
<link href="https://fonts.googleapis.com/css2?family=Noto+Sans+JP:wght@400;500;700;900&family=Noto+Serif+JP:wght@700;900&family=Oswald:wght@500;700&display=swap" rel="stylesheet">
<style>
  :root{
    --yellow:#f5e132;
    --navy:#1c2d66;
    --red:#d8232c;
    --sky-top:#1f5ea8;
    --sky-mid:#6b9fd3;
    --snow:#e9f0f7;
    --white:#ffffff;
    --ink:#1a1a1a;
  }
  *{margin:0;padding:0;box-sizing:border-box}
  html,body{width:865px;height:1200px;overflow:hidden;background:#fff}
  .poster{position:relative;width:865px;height:1200px;background:var(--yellow);overflow:hidden;font-family:"Noto Sans JP",sans-serif;color:var(--navy)}
  .brand{position:absolute;left:30px;top:30px;font-family:"Noto Sans JP",sans-serif;font-weight:500;font-size:26px;line-height:1;color:var(--navy);letter-spacing:6px}
  .host{position:absolute;left:290px;top:38px;font-size:15px;font-weight:700;color:var(--navy)}
  .title{position:absolute;left:52px;top:92px;font-family:"Noto Serif JP",serif;font-weight:900;font-size:82px;line-height:1;letter-spacing:4px;color:var(--navy)}
  .subtitle{position:absolute;left:52px;top:190px;font-family:"Noto Serif JP",serif;font-weight:900;font-size:44px;line-height:1;color:var(--navy);letter-spacing:-1px}
  .lead{position:absolute;left:52px;top:252px;font-family:"Noto Serif JP",serif;font-weight:700;font-size:22px;color:var(--navy)}
  .date{position:absolute;left:52px;top:288px;display:flex;align-items:flex-end;color:var(--navy)}
  .date-year{font-family:"Oswald",sans-serif;font-weight:700;font-size:30px;writing-mode:vertical-rl;transform:rotate(180deg);line-height:1;margin-right:6px;margin-bottom:12px}
  .date-day{font-family:"Oswald",sans-serif;font-weight:700;font-size:122px;line-height:1;letter-spacing:-2px}
  .date-week{display:flex;align-items:center;justify-content:center;width:46px;height:46px;border-radius:50%;background:var(--navy);color:var(--yellow);font-weight:900;font-size:26px;margin:0 0 18px 6px}
  .venue{position:absolute;left:447px;top:312px;width:388px;height:46px;background:var(--navy);color:var(--white);font-weight:900;font-size:27px;display:flex;align-items:center;justify-content:center;letter-spacing:1px}
  .details{position:absolute;left:447px;top:364px;font-size:13px;font-weight:700;line-height:1.4;color:var(--navy)}
  .free{position:absolute;left:722px;top:366px;width:113px;height:38px;background:var(--red);color:var(--white);font-weight:900;font-size:22px;display:flex;align-items:center;justify-content:center}
  .photo-main{position:absolute;left:0;top:432px;width:865px;height:713px;background:linear-gradient(180deg,var(--sky-top) 0%,var(--sky-mid) 38%,var(--snow) 62%,#b8c9dc 80%,#5a6f8e 100%)}
  .photo-inset{position:absolute;border:3px solid var(--white)}
  .inset-summit{left:43px;top:436px;width:230px;height:190px;background:linear-gradient(160deg,#3f73b8,#c7d5e6 60%,#8a96a8)}
  .inset-portrait{left:288px;top:436px;width:205px;height:190px;background:linear-gradient(180deg,#7ea4cf,#d9e3ee 55%,#a56a3a)}
  .inset-ice{left:518px;top:436px;width:317px;height:292px;background:linear-gradient(170deg,#dfe9f2,#9fbcd6 50%,#eef3f8)}
  .name-en{position:absolute;left:40px;top:636px;font-family:"Oswald",sans-serif;font-weight:700;color:rgba(255,255,255,.72);line-height:.92;letter-spacing:2px}
  .name-en .first{display:block;font-size:120px;padding-left:250px}
  .name-en .last{display:block;font-size:134px}
  .profile{position:absolute;left:43px;top:910px;width:240px;font-size:11px;line-height:1.55;color:var(--navy)}
  .profile strong{display:block;font-size:14px;margin-bottom:4px}
  .info-panel{position:absolute;left:560px;top:975px;width:275px;padding:12px 14px;background:rgba(255,255,255,.82);font-size:11px;line-height:1.6;color:var(--ink)}
  .info-panel strong{display:block;font-size:13px;color:var(--navy)}
  .footer{position:absolute;left:0;top:1145px;width:865px;height:55px;background:var(--navy);color:var(--white);font-size:13px;display:flex;align-items:center;justify-content:space-between;padding:0 28px}
</style>
</head>
<body>
<div class="poster">
  <div class="brand">PRV</div>
  <p class="host">一般社団法人桜台青年会議所　7月度公開例会</p>

  <h1 class="title">森川拓 講演会</h1>
  <p class="subtitle">仲間の絆～夢と希望に向かって～</p>
  <p class="lead">アルピニスト森川拓が語る、夢や希望を実現するために大切な事とは…</p>

  <div class="date">
    <span class="date-year">2013</span>
    <span class="date-day">7.14</span>
    <span class="date-week">日</span>
  </div>

  <div class="venue">桜台市民会館ホール</div>
  <p class="details">14:00～16:30（開場 13:00）<br>桜台市中央町1-2-3<br>定員：000名　TEL 0120-48-5170</p>
  <div class="free">入場無料</div>

  <div class="photo-main" role="img" aria-label="雪山の稜線と青空、尾根を登る登山者の写真"></div>
  <div class="photo-inset inset-summit" role="img" aria-label="山頂で旗を掲げる登山隊の写真"></div>
  <div class="photo-inset inset-portrait" role="img" aria-label="講師の森川拓の写真"></div>
  <div class="photo-inset inset-ice" role="img" aria-label="氷壁と氷河の写真"></div>

  <p class="name-en"><span class="first">TAKU</span><span class="last">MORIKAWA</span></p>

  <div class="profile">
    <strong>森川拓 プロフィール</strong>
    アルピニスト。七大陸最高峰の登頂を達成し、山の清掃活動や環境教育にも力を注ぐ。仲間と共に夢へ挑む大切さを各地で伝えている。
  </div>

  <div class="info-panel">
    <strong>お問い合わせ</strong>
    一般社団法人桜台青年会議所 事務局<br>
    TEL 0120-48-5170　受付 平日10:00～17:00<br>
    写真提供：森川拓事務所 (c)Taku Morikawa Office
  </div>

  <div class="footer">
    <span>主催：一般社団法人桜台青年会議所</span>
    <span>(c)Taku Morikawa Office</span>
  </div>
</div>
</body>
</html>
```